Willowmere Equine Sanctuary Flyer Urgent

Willowmere Equine Sanctuary

Rescue • Rehabilitation • Sanctuary

Willowmere Equine Sanctuary provides a safe and ethical refuge for horses, ponies and donkeys who have nowhere else to go. Some arrive needing rehabilitation and careful retraining, while others find permanent sanctuary here due to age, injury or behavioural needs.

Our mission is simple: to improve the physical and psychological wellbeing of every animal in our care.

At Willowmere we focus on:
• Rescue and rehabilitation of horses in need
• Lifetime sanctuary for those who cannot be rehomed
• Education and advocacy for responsible horse care
• Equine rehabilitation services to help horses recover and thrive

Sponsor a Horse

One of the most meaningful ways to support our work is by sponsoring one of our residents. Each horse, pony or donkey only has one sponsor!

Your sponsorship helps provide:
• Hay and feed
• Veterinary care
• Hoof trimming and routine health care
• Rugs, shelter and daily care

Many of our horses will live out their lives here, and sponsorship ensures they are safe, well fed and cared for every single day.

Sponsorship starts from $15 - $25 per week / $60 -$100 per month.

How You Can Help

• Sponsor a horse
• Make a donation
• Share our work with others

Your support helps us continue to say yes to horses who need a second chance.

📍 Willowmere Park, Victoria
📧 carla@willowmerepaddock.org

📞 0400 519 627

Font styles to use
Serif
Sans Serif

Colors
F0912C
F2A743
F7CA91
FBE8D2
FDF5EE
EE7325
F08F49
F5BC92
FAE3D3
FDF4ED

Requirements
Should not have
• Photos not provided by Willowmere

```html
<!DOCTYPE html>
<html lang="en">
<head>
<meta charset="utf-8">
<title>Willowmere Equine Sanctuary Flyer</title>
<link rel="stylesheet" href="https://fonts.googleapis.com/css2?family=Cinzel:wght@400;600;700&family=EB+Garamond:ital,wght@0,400;0,500;0,600;0,700;1,500&display=swap">
<style>
:root{
  --backdrop:#4a4a4a;
  --paper:#ffffff;
  --orange:#e27a0c;
  --orange-soft:#f0912c;
  --ink:#1c1c1c;
  --dark:#2b2b2b;
  --dark-2:#353535;
  --blue:#1414f0;
  --white:#ffffff;
}
*{box-sizing:border-box;margin:0;padding:0}
html,body{width:1200px;height:1200px;overflow:hidden;background:var(--backdrop)}
body{font-family:"EB Garamond",Georgia,serif;color:var(--ink)}
.flyer{position:absolute;left:228px;top:74px;width:744px;height:1052px;background:var(--paper);overflow:hidden}
.abs{position:absolute}

.hero{left:0;top:0;width:744px;height:366px;
  background:linear-gradient(90deg,#8a4a22 0%,#a85a2a 25%,#6b4a2a 45%,#3a2418 62%,#0b0908 75%,#000 100%)}
.brand{left:486px;top:131px;height:88px;display:flex;align-items:center;gap:8px}
.brand-name{font-family:"Cinzel",serif;font-weight:400;color:var(--white);font-size:25px;line-height:27px;text-align:right}
.brand-mark{width:50px;height:88px;background:var(--white)}

.title{left:0;top:446px;width:744px;text-align:center;font-family:"Cinzel",serif;font-weight:600;color:var(--orange);font-size:58px;line-height:64px;letter-spacing:1px;transform:translateY(-72px)}

.tagline{left:269px;top:520px;width:410px;height:33px;background:var(--dark);color:var(--white);font-family:"Cinzel",serif;font-weight:600;font-size:18px;display:flex;align-items:center;justify-content:center;gap:9px;letter-spacing:.5px}
.tagline .bar{font-weight:400;font-size:18px}

.intro{left:269px;top:568px;width:450px;font-size:11.2px;line-height:15px}

.dark-band{left:0;top:643px;width:744px;height:161px;background:linear-gradient(90deg,#2e2e2e,#3a3a3a 60%,#323232)}
.band-divider{left:425px;top:643px;width:1px;height:161px;background:#cfcfcf}
.pony{left:0;top:516px;width:225px;height:288px;
  background:linear-gradient(160deg,#d9c9a6 0%,#7a4a35 30%,#5a3526 65%,#3a2a22 100%);
  border-radius:0 70px 0 0}

.sponsor-tab{left:205px;top:670px;width:207px;height:31px;background:var(--orange);color:var(--white);font-family:"Cinzel",serif;font-size:18px;display:flex;align-items:center;justify-content:center;letter-spacing:.5px}
.sponsor-tab b{font-weight:600;margin-left:5px}
.sponsor-text{left:223px;top:711px;width:190px;color:var(--white);font-size:11.2px;line-height:15px}

.provide-title{left:437px;top:654px;font-family:"Cinzel",serif;font-weight:600;color:var(--orange);font-size:14.5px;letter-spacing:.3px}
.provide-list{left:437px;top:683px;list-style:none;color:var(--white);font-size:11.2px}
.provide-list li{height:20px;display:flex;align-items:center;gap:10px}
.tick{width:9px;height:9px;flex:none}
.provide-note{left:438px;top:770px;width:290px;color:var(--white);font-size:9.6px;line-height:14px}

.mission{left:0;top:816px;width:744px;text-align:center;color:var(--blue);font-size:13px}
.mission b{font-weight:700;letter-spacing:.2px}

.focus-band{left:0;top:848px;width:744px;height:103px;background:var(--orange)}
.focus-title{left:21px;top:870px;width:110px;color:var(--white);font-size:13.5px;line-height:18px}
.focus-line{left:138px;top:862px;width:1px;height:66px;background:var(--white)}
.focus-list{left:134px;top:855px;list-style:none;color:var(--white);font-size:10.8px;line-height:13px}
.focus-list li{display:flex;gap:6px;margin-bottom:7px}
.focus-list .tick{margin-top:2px}
.focus-divider{left:409px;top:850px;width:1px;height:99px;background:#f5bc92}
.price-head{left:422px;top:873px;width:255px;text-align:center;color:var(--white);font-size:14px;letter-spacing:.3px}
.price{top:894px;height:35px;background:var(--blue);color:var(--white);text-align:center;font-weight:700;font-size:22px;line-height:26px}
.price small{position:absolute;right:16px;bottom:1px;font-size:7.5px;font-weight:600}
.price-week{left:422px;width:120px}
.price-month{left:547px;width:130px}
.price-dot{top:905px;width:12px;height:12px;border-radius:50%;background:var(--orange)}

.help-row{left:0;top:951px;width:744px;height:49px;display:flex;align-items:center;padding-left:75px;color:var(--blue);font-size:11px}
.help-title{font-weight:700;font-size:13.5px;letter-spacing:.3px;margin-right:5px}
.help-arrow{width:8px;height:9px;margin-right:14px}
.help-item{display:flex;align-items:center;gap:6px;font-weight:600}
.help-icon{width:29px;height:29px;flex:none}
.help-sep{width:1px;height:18px;background:var(--blue);margin:0 10px}

.footer{left:0;top:1000px;width:744px;height:52px;background:var(--dark);display:flex;color:var(--white);font-size:11.2px}
.footer-quote{width:219px;background:var(--blue);font-style:italic;font-weight:500;font-size:10.8px;line-height:15px;padding:8px 0 0 21px}
.footer-cell{display:flex;align-items:center;gap:8px;border-left:1px solid #d8d8d8;padding-left:16px}
.footer-cell:first-of-type{border-left:none}
.footer-icon{width:14px;height:14px;flex:none}
</style>
</head>
<body>
<main class="flyer">
  <div class="abs hero" role="img" aria-label="Photograph of two chestnut horses touching heads against a green bush background fading to black"></div>
  <div class="abs brand">
    <div class="brand-name">Willowmere<br>Park</div>
    <div class="brand-mark"></div>
  </div>

  <h1 class="abs title">Willowmere<br>Equine Sanctuary</h1>

  <div class="abs tagline"><span>Rescue</span><span class="bar">|</span><span>Rehabilitation</span><span class="bar">|</span><span>Sanctuary</span></div>

  <p class="abs intro">Willowmere Equine Sanctuary provides a safe and ethical refuge for horses, ponies and donkeys who have nowhere else to go. Some arrive needing rehabilitation and careful retraining, while others find permanent sanctuary here due to age, injury or behavioural needs.</p>

  <div class="abs dark-band" role="img" aria-label="Muted dark photograph of horses grazing in a paddock"></div>
  <div class="abs band-divider"></div>
  <div class="abs pony" role="img" aria-label="Photograph of a brown pony with a white blaze and flaxen mane"></div>

  <div class="abs sponsor-tab">Sponsor <b>a Horse</b></div>
  <p class="abs sponsor-text">One of the most meaningful ways to support our work is by sponsoring one of our residents. Each horse, pony or donkey only has one sponsor!</p>

  <h2 class="abs provide-title">Your sponsorship helps provide:</h2>
  <ul class="abs provide-list">
    <li><svg class="tick" viewBox="0 0 10 10"><circle cx="5" cy="5" r="5" fill="#e27a0c"/><path d="M2.8 5.2l1.5 1.5 3-3" stroke="#2b2b2b" stroke-width="1.3" fill="none"/></svg>Hay and feed</li>
    <li><svg class="tick" viewBox="0 0 10 10"><circle cx="5" cy="5" r="5" fill="#e27a0c"/><path d="M2.8 5.2l1.5 1.5 3-3" stroke="#2b2b2b" stroke-width="1.3" fill="none"/></svg>Veterinary care</li>
    <li><svg class="tick" viewBox="0 0 10 10"><circle cx="5" cy="5" r="5" fill="#e27a0c"/><path d="M2.8 5.2l1.5 1.5 3-3" stroke="#2b2b2b" stroke-width="1.3" fill="none"/></svg>Hoof trimming and routine health care</li>
    <li><svg class="tick" viewBox="0 0 10 10"><circle cx="5" cy="5" r="5" fill="#e27a0c"/><path d="M2.8 5.2l1.5 1.5 3-3" stroke="#2b2b2b" stroke-width="1.3" fill="none"/></svg>Rugs, shelter and daily care</li>
  </ul>
  <p class="abs provide-note">Many of our horses will live out their lives here, and sponsorship ensures they are safe, well fed and cared for every single day.</p>

  <p class="abs mission"><b>OUR MISSION IS SIMPLE:</b> to improve the physical and psychological wellbeing of every animal in our care.</p>

  <div class="abs focus-band"></div>
  <p class="abs focus-title">AT WILLOWMERE WE FOCUS ON:</p>
  <div class="abs focus-line"></div>
  <ul class="abs focus-list">
    <li><svg class="tick" viewBox="0 0 10 10"><circle cx="5" cy="5" r="5" fill="#fff"/><path d="M2.8 5.2l1.5 1.5 3-3" stroke="#e27a0c" stroke-width="1.3" fill="none"/></svg>Rescue and rehabilitation of horses in need</li>
    <li><svg class="tick" viewBox="0 0 10 10"><circle cx="5" cy="5" r="5" fill="#fff"/><path d="M2.8 5.2l1.5 1.5 3-3" stroke="#e27a0c" stroke-width="1.3" fill="none"/></svg>Lifetime sanctuary for those who cannot be rehomed</li>
    <li><svg class="tick" viewBox="0 0 10 10"><circle cx="5" cy="5" r="5" fill="#fff"/><path d="M2.8 5.2l1.5 1.5 3-3" stroke="#e27a0c" stroke-width="1.3" fill="none"/></svg>Education and advocacy for responsible horse care</li>
    <li><svg class="tick" viewBox="0 0 10 10"><circle cx="5" cy="5" r="5" fill="#fff"/><path d="M2.8 5.2l1.5 1.5 3-3" stroke="#e27a0c" stroke-width="1.3" fill="none"/></svg><span>Equine rehabilitation services to help horses recover<br>and thrive</span></li>
  </ul>
  <div class="abs focus-divider"></div>
  <p class="abs price-head">SPONSORSHIP STARTS FROM</p>
  <div class="abs price price-week">$15 - $25<small>per week</small></div>
  <div class="abs price price-month">$60 - $100<small>per month</small></div>
  <div class="abs price-dot" style="left:416px"></div>
  <div class="abs price-dot" style="left:539px"></div>
  <div class="abs price-dot" style="left:671px"></div>

  <div class="abs help-row">
    <span class="help-title">HOW YOU CAN HELP</span>
    <svg class="help-arrow" viewBox="0 0 8 9"><path d="M0 0l8 4.5L0 9z" fill="#111"/></svg>
    <span class="help-item"><svg class="help-icon" viewBox="0 0 30 30"><circle cx="15" cy="15" r="14" fill="none" stroke="#e27a0c" stroke-width="1"/><path d="M15 21l-6-6a3.3 3.3 0 0 1 6-3.5 3.3 3.3 0 0 1 6 3.5z" fill="#e27a0c"/></svg>Sponsor a horse</span>
    <span class="help-sep"></span>
    <span class="help-item"><svg class="help-icon" viewBox="0 0 30 30"><circle cx="15" cy="15" r="14" fill="none" stroke="#e27a0c" stroke-width="1"/><rect x="9" y="14" width="12" height="8" fill="none" stroke="#e27a0c" stroke-width="1.4"/><circle cx="15" cy="10" r="3" fill="#e27a0c"/></svg>Make a donation</span>
    <span class="help-sep"></span>
    <span class="help-item"><svg class="help-icon" viewBox="0 0 30 30"><circle cx="15" cy="15" r="14" fill="none" stroke="#e27a0c" stroke-width="1"/><circle cx="15" cy="15" r="10" fill="#e27a0c"/><circle cx="18.5" cy="11" r="1.8" fill="#fff"/><circle cx="18.5" cy="19" r="1.8" fill="#fff"/><circle cx="11.5" cy="15" r="1.8" fill="#fff"/><path d="M18.5 11l-7 4 7 4" stroke="#fff" stroke-width="1" fill="none"/></svg>Share our work with others</span>
  </div>

  <footer class="abs footer">
    <p class="footer-quote">Your support helps us continue to say yes to horses who need a second chance.</p>
    <div class="footer-cell" style="width:205px;padding-left:24px"><svg class="footer-icon" viewBox="0 0 14 14"><path d="M7 13s-4.5-4.6-4.5-7.5a4.5 4.5 0 0 1 9 0C11.5 8.4 7 13 7 13z" fill="none" stroke="#e27a0c" stroke-width="1.1"/><circle cx="7" cy="5.5" r="1.6" fill="none" stroke="#e27a0c" stroke-width="1.1"/></svg>Willowmere Park, Victoria</div>
    <div class="footer-cell" style="width:123px"><svg class="footer-icon" viewBox="0 0 14 14"><path d="M3 1.5l2.2 2.6-1.3 1.6a8 8 0 0 0 4.4 4.4l1.6-1.3 2.6 2.2-1.4 1.6C6.5 12.6 1.4 7.5 1.4 3z" fill="none" stroke="#e27a0c" stroke-width="1.1"/></svg>0400 519 627</div>
    <div class="footer-cell" style="width:197px;font-size:10.8px"><svg class="footer-icon" viewBox="0 0 14 14"><rect x="1" y="3" width="12" height="8.5" fill="none" stroke="#e27a0c" stroke-width="1.1"/><path d="M1 3l6 5 6-5" fill="none" stroke="#e27a0c" stroke-width="1.1"/></svg>carla@willowmerepaddock.org</div>
  </footer>
</main>
</body>
</html>
```